Visitenkarten- und Briefpapier Design - Logo vorhanden!
Zielgruppe
Wir sind eine Projektentwicklungs GmbH die Grundstücke kauft, projektiert und wieder verkauft. Eine zukünftige GmbH ist für den Innenausbau von neuen Häusern (EFH,DHH,MFH) gedacht. Wir sind ebenfalls für den Vertrieb von Häusern tätig.
Unsere Zielgruppe sind Endkunden im Immobilienbereich die Grundstücke und/oder Häuser bis Schlüsselfertig kaufen möchten, sowie Grundstückseigentümer die verkaufen wollen.
Wir benötigen Visitenkarten UND Briefpapier.
Aufgabenstellung
Bitte vorhandenes Logo verwenden.
Briefpapier:
Es soll ein ansprechendes modernes Design sein. Wir lassen uns gerne überraschen und versuchen schnellstmöglich Feedback zu geben.
Visitenkarte:
Es soll ein ansprechendes modernes Design sein. Die Visitenkarte bitte mit 2 Seiten, auf der Rückseite könnten wir uns das Dunkle ZERANT Logo sehr gut vorstellen (nur Logo).

```html
<!DOCTYPE html>
<html lang="de">
<head>
<meta charset="utf-8">
<title>ZERANT – Briefpapier und Visitenkarten</title>
<link rel="stylesheet" href="https://fonts.googleapis.com/css2?family=EB+Garamond:wght@400;500;700&display=swap">
<style>
  :root {
    --ink: #1c1f2a;
    --paper: #ffffff;
    --card-dark: #1c1f2a;
    --rule: #1c1f2a;
    --frame: #1c1f2a;
  }
  * { margin: 0; padding: 0; box-sizing: border-box; }
  html, body { width: 849px; height: 1200px; overflow: hidden; background: var(--paper); }
  body { font-family: "EB Garamond", Georgia, serif; color: var(--ink); }

  .letterhead {
    position: relative; width: 849px; height: 1200px;
    background: var(--paper); border: 1px solid var(--frame); overflow: hidden;
  }

  .wordmark { font-weight: 400; letter-spacing: 0.02em; line-height: 1; color: var(--ink); white-space: nowrap; }
  .wordmark--letter { position: absolute; left: 57px; top: 110px; font-size: 50px; }

  .sender {
    position: absolute; left: 573px; top: 41px; height: 157px;
    border-left: 1.5px solid var(--rule); padding-left: 21px;
    font-size: 11px; line-height: 13.6px; font-style: normal;
  }
  .sender__name { font-size: 19px; font-weight: 700; line-height: 20px; letter-spacing: 0.02em; margin-top: -1px; }
  .sender__tag { margin-bottom: 14px; }
  .sender__group { margin-bottom: 14px; }
  .row { display: flex; }
  .row__label { width: 61px; }

  .fold-mark { position: absolute; left: 0; width: 27px; height: 1px; background: var(--rule); }

  .card { position: absolute; left: 326px; width: 388px; height: 226px; box-shadow: 4px 10px 16px rgba(0,0,0,0.22); overflow: hidden; }
  .card--front { top: 299px; background: var(--paper); }
  .card--back {
    top: 573px; background: var(--card-dark);
    display: flex; align-items: center; justify-content: center;
  }

  .card__person { position: absolute; left: 39px; top: 66px; }
  .card__name { font-size: 18px; font-weight: 700; line-height: 20px; }
  .card__role { font-size: 11px; line-height: 14px; }
  .card__contact { position: absolute; left: 39px; top: 127px; font-size: 11px; line-height: 13.7px; }
  .card__contact .row__label { width: 60px; }
  .wordmark--card { position: absolute; right: 50px; top: 54px; font-size: 22px; }
  .wordmark--back { font-size: 44px; color: var(--paper); letter-spacing: 0.03em; }

  .footer { position: absolute; top: 1092px; left: 0; width: 849px; height: 88px; font-size: 11px; line-height: 13.7px; text-transform: uppercase; }
  .footer__col { position: absolute; top: 4px; }
  .footer__col--company { left: 63px; }
  .footer__col--bank1 { left: 345px; }
  .footer__col--bank2 { left: 595px; }
  .footer__rule { position: absolute; top: 0; width: 1.5px; height: 87px; background: var(--rule); }
</style>
</head>
<body>
  <main class="letterhead">
    <div class="wordmark wordmark--letter">ZERANT</div>

    <address class="sender">
      <div class="sender__name">ZERANT</div>
      <div class="sender__tag">Imobilienverwaltung</div>
      <div class="sender__group">
        <div class="row"><span class="row__label">Musterstraße</span><span>123</span></div>
        <div class="row"><span class="row__label">Musterstadt</span><span>12345</span></div>
      </div>
      <div class="sender__group">
        <div class="row"><span class="row__label">Telefon:</span><span>+49 (0) 123 456789</span></div>
        <div class="row"><span class="row__label">Email:</span><span>info@zerant.com</span></div>
        <div class="row"><span class="row__label">Web:</span><span>www.zerant.com</span></div>
      </div>
      <div class="row"><span class="row__label">Steuernr.:</span><span>123/456/789</span></div>
    </address>

    <span class="fold-mark" style="top:421px"></span>
    <span class="fold-mark" style="top:597px"></span>
    <span class="fold-mark" style="top:845px"></span>

    <section class="card card--front">
      <div class="card__person">
        <div class="card__name">Max Mustermann</div>
        <div class="card__role">Musterposition</div>
      </div>
      <div class="card__contact">
        <div class="row"><span class="row__label">Telefon:</span><span>+49 (0) 123 456789</span></div>
        <div class="row"><span class="row__label">Email:</span><span>m.mustermann@zerant.com</span></div>
        <div class="row"><span class="row__label">Web:</span><span>www.zerant.com</span></div>
      </div>
      <div class="wordmark wordmark--card">ZERANT</div>
    </section>

    <section class="card card--back">
      <div class="wordmark wordmark--back">ZERANT</div>
    </section>

    <footer class="footer">
      <div class="footer__col footer__col--company">
        Mustertext<br>Firmenname<br>Geschäftsführung M. Muster<br>Firmen Steuernummer<br>Firmen USt-ID-Nr
      </div>
      <span class="footer__rule" style="left:272px"></span>
      <div class="footer__col footer__col--bank1">
        Musterbankverbindung 1<br>BLZ 123 456 78<br>Konto-Nr. 1 234 567<br>IBAN 123 456 789 123 456 789<br>BIC Muster
      </div>
      <span class="footer__rule" style="left:572px"></span>
      <div class="footer__col footer__col--bank2">
        Musterbankverbindung 2<br>BLZ 123 456 78<br>Konto-Nr. 1 234 567<br>IBAN 123 456 789 123 456 789<br>BIC Muster
      </div>
    </footer>
  </main>
</body>
</html>
```